CD Cover for singer-songwriter album

I am looking for a cover for my album „Lanterns Undertow“. I would like it to be quite artistic, preferably drawn or painted, or a collage, but other ideas are welcome. It could be emphasizing the duality of lanterns undertow, but feel free to brainstorm. The music ranges from very melancholic to funny, I am happy to provide links to the music and my previous CD Covers as references, as well as covers of other musicians I like. I will also have other upcoming projects that may need artwork so it could possibly be an ongoing colaboration with more jobs.

On the front should be:

The name of the album: Lanterns Undertow
The name of the artist: Marika Tolven

On the Back sould be the track list:
1. Hollow
2. A Quiet Hymn
3. Glassy Orchards
4. Die stille Uhr
5. Ladders
6. Nube de sal
7. Wanderlight
8. A Tin Lighthouse
9. Harbour Lullaby
10. Wandern
11. Echoes
12. Nobody counts the sparrows

References:
The music that will be on this album:
https://www.streamvale.com/user/marikatol/videos

My previous album covers:
https://marikatolven.tunecrate.com/album/paper-lanterns-on-quiet-rooftops
https://marikatolven.tunecrate.com/album/folding-rivers-in-windowpane-maps

Album covers I like:
https://benwhitlock.tunecrate.com/track/run-far
http://benwhitlock.co.uk/music/

Once chosen a front cover I would like to receive both front and back seperately and also in one file plus the file that goes on the CD for printing.

Target Market(s)

People who like folk, acoustic music, musical

Requirements
Nice to have
• Kind of vintage/retro maybe minimalistic design
Should not have
• My face on the cover

```html
<!DOCTYPE html>
<html lang="en">
<head>
<meta charset="utf-8">
<title>Lanterns Undertow — Marika Tolven</title>
<link rel="stylesheet" href="https://fonts.googleapis.com/css2?family=Titan+One&family=Cutive+Mono&display=swap">
<style>
  :root {
    --corner-grey: #666666;
    --field-dark: #333333;
    --ink: #000000;
    --paper: #ffffff;
    --brick: #952a20;
    --tag-teal: #6a9e9c;
    --skin: #f7cd9a;
    --silver: #c9c9c9;
  }
  html, body {
    margin: 0;
    padding: 0;
    width: 1200px;
    height: 1200px;
    overflow: hidden;
    background: var(--field-dark);
  }
  .cover {
    position: relative;
    width: 1200px;
    height: 1200px;
    overflow: hidden;
  }
  .cover__art {
    position: absolute;
    inset: 0;
    display: block;
  }
  .album-title {
    font-family: "Titan One", sans-serif;
    font-size: 118px;
  }
  .album-title__shadow { fill: var(--paper); }
  .album-title__face { fill: var(--brick); }
  .artist-tag__name {
    font-family: "Cutive Mono", "Courier New", monospace;
    font-size: 46px;
  }
</style>
</head>
<body>
<main class="cover">
  <svg class="cover__art" viewBox="0 0 1200 1200" width="1200" height="1200" xmlns="http://www.w3.org/2000/svg">
    <defs>
      <clipPath id="sunburst-area">
        <rect x="820" y="0" width="380" height="420"/>
      </clipPath>
      <radialGradient id="portrait-tones" cx="0.5" cy="0.62" r="0.62">
        <stop offset="0" stop-color="#f7cd9a"/>
        <stop offset="0.38" stop-color="#f2c08e"/>
        <stop offset="0.62" stop-color="#952a20"/>
        <stop offset="0.86" stop-color="#5a1a14"/>
        <stop offset="1" stop-color="#151515"/>
      </radialGradient>
    </defs>

    <!-- backdrop -->
    <rect class="backdrop" width="1200" height="1200" fill="var(--corner-grey)"/>
    <g class="sunburst" clip-path="url(#sunburst-area)" fill="var(--brick)">
      <polygon points="1100,620 900,0 940,0"/>
      <polygon points="1100,620 985,0 1030,0"/>
      <polygon points="1100,620 1070,0 1115,0"/>
      <polygon points="1100,620 1160,0 1210,0"/>
      <polygon points="1100,620 1250,40 1250,90"/>
      <polygon points="1100,620 1250,140 1250,190"/>
      <polygon points="1100,620 1250,240 1250,290"/>
      <polygon points="1100,620 1250,330 1250,380"/>
    </g>
    <path class="backdrop__field" fill="var(--field-dark)"
      d="M0,80 Q60,30 130,0 L870,0 C1030,90 1150,220 1200,330 L1200,1075 Q1175,1140 1145,1200 L0,1200 Z"/>

    <!-- scattered squares -->
    <g class="confetti" fill="var(--brick)">
      <rect x="57" y="176" width="32" height="44"/>
      <rect x="160" y="295" width="80" height="72" transform="rotate(37 200 331)"/>
      <rect x="1016" y="300" width="34" height="42" transform="rotate(20 1033 321)"/>
      <rect x="1092" y="1030" width="32" height="44"/>
    </g>

    <!-- burst strokes -->
    <g class="burst">
      <polygon points="125,542 178,578 131,552" fill="var(--paper)"/>
      <polygon points="125,542 178,578 131,536" fill="var(--brick)"/>
      <polygon points="55,590 167,640 62,575" fill="var(--paper)"/>
      <polygon points="62,575 167,640 66,567" fill="var(--brick)"/>
      <polygon points="84,829 140,806 89,836" fill="var(--paper)"/>
      <polygon points="84,822 140,806 84,829" fill="var(--brick)"/>
      <polygon points="80,946 196,938 78,935" fill="var(--paper)"/>
      <polygon points="75,926 196,938 78,935" fill="var(--brick)"/>
      <polygon points="1060,530 1110,503 1104,494" fill="var(--paper)"/>
      <polygon points="1060,530 1104,494 1108,490" fill="var(--brick)"/>
      <polygon points="1080,652 1190,608 1186,596" fill="var(--paper)"/>
      <polygon points="1080,652 1186,596 1186,585" fill="var(--brick)"/>
      <polygon points="1093,771 1152,774 1152,765" fill="var(--paper)"/>
      <polygon points="1093,771 1152,765 1152,760" fill="var(--brick)"/>
      <polygon points="1073,845 1130,953 1140,948" fill="var(--paper)"/>
      <polygon points="1073,845 1140,948 1152,940" fill="var(--brick)"/>
    </g>

    <!-- album title -->
    <g class="album-title">
      <text class="album-title__shadow" x="152" y="131" textLength="620" lengthAdjust="spacingAndGlyphs" transform="skewX(-10)" transform-origin="465 100">Lanterns</text>
      <text class="album-title__face" x="148" y="127" textLength="620" lengthAdjust="spacingAndGlyphs" transform="skewX(-10)" transform-origin="465 100">Lanterns</text>
      <text class="album-title__shadow" x="476" y="220" textLength="558" lengthAdjust="spacingAndGlyphs" transform="skewX(-10)" transform-origin="755 190">Undertow</text>
      <text class="album-title__face" x="472" y="216" textLength="558" lengthAdjust="spacingAndGlyphs" transform="skewX(-10)" transform-origin="755 190">Undertow</text>
    </g>

    <!-- illustration area -->
    <path class="portrait" role="img"
      aria-label="Comic-style illustration of a red-haired woman wearing large silver headphones, looking straight ahead"
      d="M170,1121 L170,720 C170,420 370,224 600,222 C830,224 1050,420 1050,720 L1050,1121 Z"
      fill="url(#portrait-tones)" stroke="var(--ink)" stroke-width="8"/>

    <!-- bottom band -->
    <rect class="footer-band" x="0" y="1121" width="1200" height="30" fill="var(--ink)"/>
    <g class="footer-blocks" fill="var(--brick)">
      <rect x="12" y="1152" width="28" height="40"/>
      <rect x="246" y="1151" width="500" height="49"/>
      <rect x="925" y="1146" width="32" height="44"/>
      <rect x="1132" y="1113" width="68" height="87"/>
    </g>

    <!-- artist tag -->
    <g class="artist-tag">
      <polygon points="23,1088 65,1155 360,1025 390,953 309,942" fill="var(--tag-teal)" stroke="var(--paper)" stroke-width="5" stroke-linejoin="round"/>
      <g transform="rotate(-24 210 1050)">
        <text class="artist-tag__name" x="62" y="1068" fill="var(--paper)" textLength="300" lengthAdjust="spacingAndGlyphs">Marika Tolven</text>
        <text class="artist-tag__name" x="60" y="1066" fill="var(--ink)" textLength="300" lengthAdjust="spacingAndGlyphs">Marika Tolven</text>
      </g>
    </g>
  </svg>
</main>
</body>
</html>
```